Design a double sided business card

We are looking for a clean, eye-catching, and contemporary design that enhances the brand and presents a premium, professional image. Our preference is for a brown card with black gloss detailing and embossed elements; however, we are open to creative input and design suggestions that best achieve a strong visual impact.

Please see the attached existing business card for reference. We use both black and brown colours consistently across our branding.

On sample provided

```html
<!DOCTYPE html>
<html lang="en">
<head>
<meta charset="utf-8">
<title>Stonewell – Business Card</title>
<link rel="stylesheet" href="https://fonts.googleapis.com/css2?family=Libre+Baskerville&family=Montserrat:wght@500;700&display=swap">
<style>
  :root {
    --backdrop: #b9805c;
    --kraft: #dcaa80;
    --kraft-edge: #c77a2e;
    --brand-orange: #b8641c;
    --ink: #1b1512;
    --card-black: #1e1b20;
    --black-emboss: #47434b;
  }
  * { box-sizing: border-box; margin: 0; padding: 0; }
  html, body { width: 1200px; height: 800px; overflow: hidden; }
  body {
    background: var(--backdrop);
    display: flex;
    align-items: center;
    justify-content: center;
    gap: 48px;
    font-family: "Montserrat", sans-serif;
  }
  .card {
    position: relative;
    width: 525px;
    height: 300px;
    border-radius: 3px;
    box-shadow: 0 14px 30px rgba(60, 25, 5, 0.35);
  }
  .card--front {
    background: var(--kraft);
    border-bottom: 3px solid var(--kraft-edge);
    color: var(--ink);
  }
  .card--back {
    background: var(--card-black);
    border-bottom: 3px solid var(--kraft-edge);
    display: flex;
    align-items: center;
    justify-content: center;
  }
  .brand {
    display: flex;
    align-items: center;
    gap: 12px;
    font-family: "Montserrat", sans-serif;
    font-weight: 700;
    letter-spacing: 0.18em;
    text-transform: uppercase;
  }
  .brand__square { display: block; }
  .card--front .brand {
    position: absolute;
    top: 44px;
    left: 128px;
    font-size: 26px;
    color: var(--brand-orange);
  }
  .card--front .brand__square { width: 30px; height: 30px; background: var(--brand-orange); }
  .card--back .brand { font-size: 40px; color: var(--black-emboss); }
  .card--back .brand__square { width: 44px; height: 44px; background: var(--black-emboss); }
  .person {
    position: absolute;
    top: 118px;
    left: 36px;
  }
  .person__name {
    font-family: "Libre Baskerville", serif;
    font-size: 22px;
    color: var(--brand-orange);
    line-height: 1.1;
  }
  .person__role { font-size: 14px; font-weight: 500; margin-top: 2px; }
  .contact {
    position: absolute;
    right: 34px;
    bottom: 30px;
    font-size: 12.5px;
    font-weight: 500;
    line-height: 1.45;
    list-style: none;
  }
  .contact__address { margin-bottom: 2px; }
  .contact__item { display: flex; align-items: center; gap: 7px; }
  .contact__icon { width: 12px; height: 12px; flex: none; fill: var(--brand-orange); }
</style>
</head>
<body>
  <section class="card card--front" aria-label="Business card front">
    <div class="brand"><span class="brand__name">Stonewell</span><span class="brand__square"></span></div>
    <div class="person">
      <p class="person__name">Ravi Mehta</p>
      <p class="person__role">Director</p>
    </div>
    <ul class="contact">
      <li class="contact__address">12 Mill Court<br>Harlow Green HG4 2PL</li>
      <li class="contact__item">
        <svg class="contact__icon" viewBox="0 0 12 12"><path d="M1 3c0-1 1-2 3-2l1 2-1.5 1c.5 1.5 1.5 2.5 3 3l1-1.5 2 1c0 2-1 3-2 3C4 9.5 1.5 7 1 3z"/></svg>
        0800 555 0142</li>
      <li class="contact__item">
        <svg class="contact__icon" viewBox="0 0 12 12"><path d="M3 0h6v12H3zM4 1.5v8h4v-8zM5.5 10.3h1v1h-1z" fill-rule="evenodd"/></svg>
        07700 900461</li>
      <li class="contact__item">
        <svg class="contact__icon" viewBox="0 0 12 12"><path d="M0 2h12v8H0zM1 3l5 3.5L11 3v-.2H1z" fill-rule="evenodd"/></svg>
        ravi@stonewell.co.uk</li>
      <li class="contact__item">
        <svg class="contact__icon" viewBox="0 0 12 12"><circle cx="6" cy="6" r="5.5"/><path d="M1 6h10M6 .5c-2 2-2 9 0 11M6 .5c2 2 2 9 0 11" stroke="#dcaa80" stroke-width="0.8" fill="none"/></svg>
        www.stonewell.co.uk</li>
    </ul>
  </section>

  <section class="card card--back" aria-label="Business card back">
    <div class="brand"><span class="brand__name">Stonewell</span><span class="brand__square"></span></div>
  </section>
</body>
</html>
```